Roofing Company Modern look

I want a modern and sophisticated look for our roofing business.

Our address is :

4276 Pellman Crossing Rd
Orlando, Fl 32825

(407)-583-2716

www.SummitcrestShinglesFl.com

I also want to make sure on the back there is a spot to put
Project Manager Name :

Number:

Because the cards will be used by all sales people

Project Manager Name :

Also there are accreditation we have logos are uploaded here as well that I would like maybe on the back of card as well

I also want to highlight our special attributions or trades:

Residential & Commercial
Fully Insured
License # CCC4872196
Insurance Claims
Serving Central Florida Since 1992
Free Estimates

Contact Information for Business Card

Our address is :

4276 Pellman Crossing Rd
Orlando, Fl 32825

(407)-583-2716

Project Manager Name :

Residential & Commercial
Fully Insured
License # CCC4872196
Insurance Claims
Free Estimates

Font styles to use
Serif
Sans Serif

Colors
3176b5

Requirements
Must have
• Must have royal blue like my logo grey and black are the colors I like

```html
<!DOCTYPE html>
<html lang="en">
<head>
<meta charset="utf-8">
<title>Summitcrest Roofing &amp; Gutters – Business Card</title>
<link rel="stylesheet" href="https://fonts.googleapis.com/css2?family=Kumbh+Sans:wght@400;500;600;700&display=swap">
<style>
  :root {
    --blue-light: #2fa3df;
    --blue-mid: #2178cf;
    --blue-deep: #1552ad;
    --brand-blue: #3176b5;
    --ink: #1b1b1b;
    --grey: #6d7278;
    --paper: #ffffff;
    --page: #e9ebee;
    --mark-tint: rgba(210, 225, 245, .28);
  }
  * { box-sizing: border-box; margin: 0; padding: 0; }
  html, body {
    width: 1200px; height: 900px; overflow: hidden;
    background: var(--page);
    font-family: "Kumbh Sans", sans-serif;
  }
  .canvas {
    position: relative; width: 1200px; height: 900px;
    display: flex; flex-direction: column; align-items: center; justify-content: center; gap: 40px;
  }
  .card {
    position: relative; width: 700px; height: 400px; overflow: hidden;
    box-shadow: 0 6px 20px rgba(0,0,0,.18);
  }

  /* ---------- Front ---------- */
  .card--front { background: var(--paper); }
  .front__brand {
    position: absolute; left: 0; right: 0; top: 70px;
    display: flex; flex-direction: column; align-items: center; gap: 6px;
    color: var(--brand-blue); font-weight: 600;
  }
  .brand__dot {
    width: 46px; height: 46px; border-radius: 50%; background: var(--brand-blue);
    margin-bottom: 6px;
  }
  .brand__name { font-size: 40px; letter-spacing: 5px; line-height: 1; }
  .brand__sub { font-size: 12.5px; letter-spacing: 3.5px; }
  .front__band {
    position: absolute; left: 0; right: 0; bottom: 0; height: 165px;
    background: linear-gradient(180deg, var(--blue-light) 0%, var(--blue-mid) 55%, var(--blue-deep) 100%);
  }
  .contact {
    position: absolute; display: flex; align-items: center; gap: 12px;
    color: var(--ink); font-size: 14px; font-weight: 500; letter-spacing: 1px;
  }
  .contact__icon {
    flex: none; width: 26px; height: 26px; border-radius: 50%; background: var(--ink);
    display: flex; align-items: center; justify-content: center;
  }
  .contact__icon svg { width: 14px; height: 14px; }
  .contact--address { right: 46px; top: 20px; line-height: 1.25; }
  .contact--phone { left: 46px; top: 78px; }
  .contact--web { left: 46px; top: 114px; }

  /* ---------- Back ---------- */
  .card--back {
    background: linear-gradient(180deg, var(--blue-light) 0%, var(--blue-mid) 50%, var(--blue-deep) 100%);
    color: var(--paper);
  }
  .back__person { position: absolute; right: 62px; top: 38px; text-align: right; }
  .person__name { font-size: 27px; font-weight: 600; letter-spacing: 2px; }
  .person__title { font-size: 20px; font-weight: 500; margin-top: 2px; }
  .back__tab { position: absolute; right: 0; top: 44px; width: 16px; height: 48px; background: var(--paper); }
  .back__mark {
    position: absolute; right: 44px; top: 128px; width: 280px;
    display: flex; flex-direction: column; align-items: center; gap: 6px;
    color: var(--mark-tint); font-weight: 600;
  }
  .back__mark .brand__dot { width: 80px; height: 80px; background: var(--mark-tint); margin-bottom: 4px; }
  .back__mark .brand__name { font-size: 31px; letter-spacing: 3px; }
  .back__mark .brand__sub { font-size: 10px; letter-spacing: 2.6px; }
  .services {
    position: absolute; left: 56px; top: 168px; list-style: none;
    font-size: 17px; font-weight: 500; line-height: 1.5; letter-spacing: .4px;
  }
  .services li::before { content: "•"; margin-right: 7px; font-size: 12px; vertical-align: 2px; }
  .badges {
    position: absolute; right: 48px; bottom: 34px;
    display: flex; align-items: center; gap: 18px;
  }
  .badge { background: var(--paper); }
  .badge--rating { width: 28px; height: 38px; border-radius: 4px; }
  .badge--applicator { width: 40px; height: 40px; background: #3a3a3a; transform: rotate(45deg) scale(.8); }
  .badge--contractor { width: 126px; height: 38px; border: 2px solid #c8202b; }
  .badge--listing { width: 44px; height: 44px; border-radius: 50%; background: #dfe3e8; border: 3px solid #556070; }
</style>
</head>
<body>
<main class="canvas">

  <section class="card card--front" aria-label="Business card front">
    <div class="front__brand">
      <span class="brand__dot"></span>
      <span class="brand__name">SUMMITCREST</span>
      <span class="brand__sub">ROOFING &amp; GUTTERS INC.</span>
    </div>
    <div class="front__band">
      <div class="contact contact--address">
        <span class="contact__icon">
          <svg viewBox="0 0 16 16"><path d="M8 2 1.5 7.5h2V14h3.5v-4h2v4h3.5V7.5h2z" fill="#fff"/></svg>
        </span>
        <span>4276 Pellman Crossing Rd<br>Orlando, Fl 32825</span>
      </div>
      <div class="contact contact--phone">
        <span class="contact__icon">
          <svg viewBox="0 0 16 16"><path d="M2 6c0-2 2-3 6-3s6 1 6 3v1h-3V5.5H5V7H2z M4 8h8l1 5H3z" fill="#fff"/><circle cx="8" cy="10.5" r="1.4" fill="#1b1b1b"/></svg>
        </span>
        <span>(407)-583-2716</span>
      </div>
      <div class="contact contact--web">
        <span class="contact__icon">
          <svg viewBox="0 0 16 16" fill="none" stroke="#fff" stroke-width="1.4"><circle cx="8" cy="8" r="6"/><ellipse cx="8" cy="8" rx="2.6" ry="6"/><path d="M2 8h12"/></svg>
        </span>
        <span>www.SummitcrestShinglesFl.com</span>
      </div>
    </div>
  </section>

  <section class="card card--back" aria-label="Business card back">
    <div class="back__mark" aria-hidden="true">
      <span class="brand__dot"></span>
      <span class="brand__name">SUMMITCREST</span>
      <span class="brand__sub">ROOFING &amp; GUTTERS INC.</span>
    </div>
    <div class="back__tab"></div>
    <div class="back__person">
      <p class="person__name">PERSON NAME HERE</p>
      <p class="person__title">Job Tittle</p>
    </div>
    <ul class="services">
      <li>Residential &amp; Commercial</li>
      <li>Fully Insured</li>
      <li>License # CCC4872196</li>
      <li>Insurance Claims</li>
      <li>Serving Central Florida Since 1992</li>
      <li>Free Estimates</li>
    </ul>
    <div class="badges" role="img" aria-label="Accreditation badges">
      <span class="badge badge--rating"></span>
      <span class="badge badge--applicator"></span>
      <span class="badge badge--contractor"></span>
      <span class="badge badge--listing"></span>
    </div>
  </section>

</main>
</body>
</html>
```